Business Card Design Project 4 Construction Business

I am after a creative, but sleek and simple/ clean business card design. This design will form the basis of future items and might include a logo or simply a creative way to lay out the text of my company name 'kestrel ventures'
I like the simplicity of black and white however I would also be happy to see a splash of colour introduced somehow to give the text some interest and make it stand out.
I would like a double sided card.
I am young (ish!) and professional, offering construction and project management services, what I don't want is the traditional builders type card featuring a cheesy hammer/ saw image etc.
As the company name, kestrel ventures, suggests, we focus on working closely and collaboratively together, in synergy with all stakeholders involved in the projects that we undertake
Construction

```html
<!DOCTYPE html>
<html lang="en">
<head>
<meta charset="utf-8">
<title>Kestrel Ventures – Business Card</title>
<link rel="stylesheet" href="https://fonts.googleapis.com/css2?family=Roboto:wght@400;700&display=swap">
<style>
  :root {
    --paper: #ffffff;
    --stage: #eceded;
    --charcoal: #3a3a3a;
    --card-dark: #2f2f2f;
    --band-dark: #1b1b1b;
    --ink: #2b2b2b;
    --orange: #f39a2b;
    --light-text: #e9e9e9;
  }
  * { box-sizing: border-box; margin: 0; padding: 0; }
  html, body { width: 1200px; height: 1000px; overflow: hidden; }
  body {
    position: relative;
    background: var(--stage);
    font-family: "Roboto", Arial, sans-serif;
    color: var(--ink);
  }

  .card {
    position: absolute;
    width: 500px;
    height: 300px;
    top: 260px;
    box-shadow: 0 8px 22px rgba(0,0,0,0.12);
    overflow: hidden;
  }
  .card--front { left: 70px; background: var(--paper); }
  .card--back  { left: 630px; background: var(--card-dark); }

  .brand {
    display: flex;
    align-items: center;
    gap: 10px;
    white-space: nowrap;
  }
  .brand__mark {
    width: 26px; height: 26px;
    background: var(--orange);
    flex: none;
  }
  .brand__name {
    font-weight: 700;
    font-size: 24px;
    letter-spacing: 2px;
    text-transform: uppercase;
    line-height: 1;
    white-space: nowrap;
  }
  .card--front .brand { position: absolute; top: 34px; left: 120px; }
  .card--front .brand__name { color: var(--ink); }

  .contact {
    position: absolute;
    left: 42px;
    top: 104px;
    list-style: none;
    font-size: 12px;
    line-height: 1.45;
    color: var(--ink);
  }
  .contact__item { display: flex; align-items: flex-start; gap: 10px; }
  .contact__icon { width: 12px; height: 12px; margin-top: 2px; flex: none; }

  .person {
    position: absolute;
    right: 40px;
    top: 168px;
    text-align: right;
  }
  .person__name { color: var(--orange); font-weight: 700; font-size: 19px; }
  .person__role { font-size: 12px; color: var(--ink); margin-top: 2px; }

  .accent-block {
    position: absolute;
    right: 0; top: 214px;
    width: 14px; height: 26px;
    background: var(--orange);
  }

  .footer-band {
    position: absolute;
    left: 0; bottom: 0;
    width: 100%; height: 44px;
    background: var(--charcoal);
    display: flex; align-items: center;
    padding-left: 42px;
  }
  .footer-band__web { color: var(--light-text); font-size: 12px; font-weight: 700; letter-spacing: 0.3px; }

  .card--back .brand {
    position: absolute;
    top: 112px; left: 0; right: 0;
    justify-content: center;
  }
  .card--back .brand__name { color: var(--paper); }
  .card--back .back__web {
    position: absolute; top: 156px; left: 0; right: 0;
    text-align: center; color: var(--light-text);
    font-size: 12px; font-weight: 700;
    white-space: nowrap;
  }

  .showcase-band {
    position: absolute;
    left: 0; bottom: 0;
    width: 1200px; height: 152px;
    background: var(--band-dark);
  }
  .showcase-band .brand { position: absolute; right: 90px; top: 50px; gap: 16px; }
  .showcase-band .brand__mark { width: 48px; height: 48px; }
  .showcase-band .brand__name { color: var(--paper); font-size: 44px; letter-spacing: 3px; }
</style>
</head>
<body>

  <section class="card card--front" aria-label="Card front">
    <div class="brand">
      <span class="brand__mark"></span>
      <span class="brand__name">Kestrel Ventures</span>
    </div>

    <ul class="contact">
      <li class="contact__item">
        <svg class="contact__icon" viewBox="0 0 12 12"><path d="M6 1 1 5.5h1.5V11h3V8h1v3h3V5.5H11z" fill="var(--orange)"/></svg>
        <span>14 Calder St<br>Northbridge NSW 2063</span>
      </li>
      <li class="contact__item">
        <svg class="contact__icon" viewBox="0 0 12 12"><path d="M3 1h2l1 3-1.5 1a6 6 0 0 0 2.5 2.5L8 6l3 1v2a2 2 0 0 1-2 2A8 8 0 0 1 1 3a2 2 0 0 1 2-2z" fill="var(--orange)"/></svg>
        <span>0400 555 018</span>
      </li>
      <li class="contact__item">
        <svg class="contact__icon" viewBox="0 0 12 12"><rect x="1" y="2.5" width="10" height="7" fill="var(--orange)"/><path d="M1 2.5 6 6.5l5-4" stroke="#fff" stroke-width="1" fill="none"/></svg>
        <span>owen@kestrelventures.com.au</span>
      </li>
    </ul>

    <div class="person">
      <p class="person__name">Owen Hartley</p>
      <p class="person__role">Director</p>
    </div>
    <span class="accent-block"></span>

    <div class="footer-band">
      <span class="footer-band__web">www.kestrelventures.com.au</span>
    </div>
  </section>

  <section class="card card--back" aria-label="Card back">
    <div class="brand">
      <span class="brand__mark"></span>
      <span class="brand__name">Kestrel Ventures</span>
    </div>
    <p class="back__web">www.kestrelventures.com.au</p>
  </section>

  <footer class="showcase-band">
    <div class="brand">
      <span class="brand__mark"></span>
      <span class="brand__name">Kestrel Ventures</span>
    </div>
  </footer>

</body>
</html>
```